依頼詳細
表面はカラー、裏面は白黒で申し込み用紙にしようと考えています。
魅力のあるツアーだと思いますので、読み手に伝わるよう作成をお願いします。
〈ツアーのポイント〉
・透き通った青い海、緑の山々、満天の星空など、大自然に囲まれたダイナミックな眺望
・貸切バスで観光スポットをご案内
・地元の食材にこだわった料理を堪能
・島人との交流
・自然の中でBBQ、キャンプファイヤー
・宿泊は神津島唯一の温泉宿
・カップル成立で特典付き
・格安
など
多少変更が出るかもしれませんので、こちらでも編集できる形式で納品をお願いします。
ご不明点などありましたらご連絡ください。
よろしくお願いいたします。
記載項目
表現など変更して頂いて結構です。

【表面】
独身女性参加者募集
〈イベント名称〉渚トーク星結び
〈日時〉2015年7月3日(金)~2015年7月5日(日)
〈会場〉神津島
〈ツアースケジュール〉
1日目 20:00 東京 灯波客船ターミナル集合(女性のみ)・女子会
23:00 出航(大型客船)
2日目 9:00 神津島着・チェックイン
朝 男性合流・アイスブレイク
昼 昼食・島内観光
夜 BBQ・キャンプファイヤー・温泉旅館宿泊
3日目 朝 自由時間
13:35 神津島発
17:30 東京 灯波客船ターミナル着・解散
〈ツアーのポイント〉依頼詳細参考
〈集合場所〉白浪航路灯波港 1階ロビー ※若葉環状線蓮見坂駅から徒歩8分
〈集合時間〉2015年7月3日(金)20:00
〈参加対象〉20歳~35歳の島外在住独身女性
〈募集人数〉15名(先着順)
〈参加料金〉15,000円/1人(交通費・宿泊費・食費込み)
〈申込方法〉裏面の申込書にご記入の上、メール・FAX・郵送にてお申込みください。
〈申込締切〉2015年6月7日(日)
〈ホームページ〉
※ホームページのURLを載せたいのですが、まだ出来上がっていないので後ほどURLを追加できるようにしていただきたいです。

裏面は補足情報に記載します。
サイズ
A4
ページ数
両面
希望イメージ
• +5 0 +5
• シンプル
複雑
• 単色
カラフル
• 暗い
明るい
• 日常
高級
• 遊び心
厳粛
• 未来的
伝統的
• 女性的
男性的
希望する色
赤系、水色系、緑系、黄・オレンジ系
納品ファイル
補足説明
【裏面】申込用紙
〈イベント名称〉
〈日時〉
〈会場〉
〈募集人数〉15名(先着順)
〈参加資格〉20歳から35歳までの神津島外在住の独身女性
お一人様参加・シングルマザー・結婚歴あり歓迎
〈参加料金〉
MAIL  shiomi@hx.nagisanet-example.jp
メールでのお申し込みは①氏名②生年月日③住所④電話番号⑤メールアドレスを添えて上記のアドレスまでご送信ください。
FAX 04992-7-5530
〈申し込みフォーム〉
・氏名(ふりがな)
・氏名
・生年月日
・電話番号
・メールアドレス
・自己PR
〈注意事項〉
1 申し込み・キャンセルは6月7日(日)までにお願いします。
2 男女比は出来る限り調整しますが同数にならないこともありますのでご了承願います。
3 個人情報は厳重に管理し、本事業のみの使用とさせていただきます。
4 悪天候時はプログラム内容を変更または中止する場合があります。

申し込み受付後、事務局より順次詳細をお送りいたします。

問い合わせ・お申込み 汐見村商工会青年部事務局
〒100-0999 東京都汐見村汐見村2483番地
TEL  04992-7-4418
FAX  04992-7-5530

依頼公開後の追記内容
写真を添付します。

ターゲット層を対象にアンケート調査を実施した結果、最も多く票が集まったため。

この度は私どもの為に、多数ご提案をご用意していただき、誠にありがとうございます。どの提案も魅力を感じていましたが、上記の理由から一社選ばせていただきました。
折角親身にお世話をしていただいたところ、心苦しい限りですが、ご理解いただければ幸いです。
また、同様の機会があればよろしくお願いいたします。

```html
<!DOCTYPE html>
<html lang="ja">
<head>
<meta charset="utf-8">
<title>渚トーク星結び 申込用紙</title>
<link rel="stylesheet" href="https://fonts.googleapis.com/css2?family=Noto+Sans+JP:wght@400;500;700;900&family=M+PLUS+Rounded+1c:wght@500;800&display=swap">
<style>
:root{
  --ink:#1a1a1a;
  --mid:#555;
  --line:#9a9a9a;
  --pale:#e6e6e6;
  --paper:#ffffff;
  --sky-top:#5c5c5c;
  --sky-low:#d4d4d4;
}
*{margin:0;padding:0;box-sizing:border-box}
html,body{width:851px;height:1200px;overflow:hidden;background:var(--paper)}
body{font-family:"Noto Sans JP",sans-serif;color:var(--ink);position:relative}
.sky-photo{position:absolute;left:0;top:0;width:851px;height:250px;
  background:linear-gradient(180deg,var(--sky-top) 0%,#9b9b9b 45%,var(--sky-low) 80%,var(--paper) 100%)}
.recruit{position:absolute;left:30px;top:22px;font-size:32px;font-weight:900;color:var(--paper);letter-spacing:1px;
  text-shadow:0 0 4px rgba(0,0,0,.6)}
.tour-tag{position:absolute;left:560px;top:14px;text-align:center;color:var(--paper)}
.tour-tag small{display:block;font-size:13px;font-weight:700}
.tour-tag span{display:inline-block;font-size:30px;font-weight:900;font-family:"M PLUS Rounded 1c",sans-serif;
  text-shadow:0 0 4px rgba(0,0,0,.6)}
.event-title{position:absolute;left:30px;top:64px;font-family:"M PLUS Rounded 1c",sans-serif;font-weight:800;
  font-size:62px;line-height:1;color:var(--ink);letter-spacing:2px}
.event-date{position:absolute;left:30px;top:130px;font-size:31px;font-weight:900;letter-spacing:.5px;line-height:1.3}
.event-date .dow{display:inline-block;width:28px;height:28px;border-radius:50%;background:var(--ink);color:var(--paper);
  font-size:17px;text-align:center;line-height:28px;vertical-align:4px}
.event-date .venue{margin-left:22px}
.facts{position:absolute;left:30px;top:180px;font-size:14px;line-height:1.65}
.ship-photo{position:absolute;left:548px;top:262px;width:272px;height:140px;
  background:linear-gradient(180deg,#1e1e1e 0%,#3a3a3a 60%,#151515 100%)}
.depart{position:absolute;left:756px;top:244px;width:70px;height:70px;border-radius:50%;background:var(--paper);
  border:2px solid var(--ink);text-align:center;font-weight:900;font-size:16px;line-height:1.15;padding-top:14px}
.lead{position:absolute;left:30px;top:264px;width:500px;font-size:18px;line-height:1.95;font-weight:500}
.apply-head{position:absolute;left:30px;top:486px;font-size:24px;font-weight:900;display:flex;align-items:center;gap:8px;line-height:1.3}
.contact-row{position:absolute;left:30px;display:flex;align-items:center;gap:14px}
.contact-row .badge{width:48px;height:48px;border-radius:50%;background:var(--ink);color:var(--paper);
  font-size:13px;font-weight:900;display:flex;align-items:center;justify-content:center}
.contact-row .value{font-size:30px;font-weight:700;letter-spacing:.5px;line-height:1.2}
.mail-row{top:530px}
.mail-note{position:absolute;left:30px;top:584px;font-size:11px;color:var(--mid)}
.fax-row{top:604px}
.fax-row .value{font-size:34px;font-weight:900}
.form{position:absolute;left:30px;top:666px;width:790px;border:2px solid var(--ink);border-collapse:collapse;font-size:13px}
.form caption{caption-side:top;background:var(--pale);border:2px solid var(--ink);border-bottom:none;
  font-size:16px;font-weight:700;padding:4px 0}
.form td{border:1px solid var(--line);vertical-align:top;padding:4px 8px}
.form .kana td{height:22px;font-size:11px;border-bottom:1px dashed var(--line)}
.form .name td{height:48px}
.form .birth td{height:52px}
.form .birth .era{font-size:15px;padding-top:6px}
.form .mail td{height:48px}
.form .pr td{height:80px}
.notes{position:absolute;left:30px;top:980px;width:440px;font-size:12px;line-height:1.75}
.notes h3{font-size:13px;font-weight:700}
.notes ol{list-style:none}
.notes li{display:flex;gap:6px}
.notes .after{margin-top:4px;font-size:11.5px}
.office{position:absolute;left:486px;top:984px;width:334px;border:1.5px solid var(--ink);padding:10px 12px;
  font-size:12px;line-height:1.7}
.office strong{font-size:13px}
</style>
</head>
<body>
<div class="sky-photo" role="img" aria-label="星空と雲が広がる島の夜空、ハートを描く光の軌跡"></div>

<p class="recruit">独身女性参加者募集</p>
<div class="tour-tag"><small>トーク×恋×3日間</small><span>婚活ツアー</span></div>
<h1 class="event-title">渚トーク星結び</h1>
<p class="event-date">2015年7月3日<span class="dow">金</span>〜7月5日<span class="dow">日</span><span class="venue">会場：神津島</span></p>

<div class="facts">
  <p>〈募集人数〉15名（先着順）</p>
  <p>〈参加資格〉20歳から35歳までの神津島外在住の独身女性、お一人様参加・シングルマザー・結婚歴あり歓迎</p>
  <p>〈参加料金〉15,000円／1人（交通費・宿泊費・食費込み）</p>
</div>

<div class="ship-photo" role="img" aria-label="夜の港に停泊するライトアップされた大型客船"></div>
<div class="depart">23:00<br>出航!</div>

<p class="lead">この日から始まる!出会いの３日間。<br>男性との素敵な出会いはもちろん、女性の方とも仲良くなれます。交流時間が長く取れるので、打ち解けやすく、ワクワク、ドキドキの素敵な島のロケーションで楽しく新しい出会いをゲットしましょう!</p>

<p class="apply-head">
  <svg width="26" height="26" viewBox="0 0 28 28" aria-hidden="true"><path d="M4 24l3-9L19 3l6 6-12 12z" fill="none" stroke="#1a1a1a" stroke-width="2.4" stroke-linejoin="round"/><path d="M7 15l6 6" stroke="#1a1a1a" stroke-width="2"/></svg>
  お申し込みはコチラ♪
</p>

<div class="contact-row mail-row"><span class="badge">MAIL</span><span class="value">shiomi@hx.nagisanet-example.jp</span></div>
<p class="mail-note">メールでのお申し込みは①氏名②生年月日③住所④電話番号⑤メールアドレスを添えて上記のアドレスまでご送信ください。</p>
<div class="contact-row fax-row"><span class="badge">FAX</span><span class="value">04992-7-5530</span></div>

<table class="form">
  <caption>申し込みフォーム</caption>
  <tr class="kana"><td style="width:50%">フリガナ</td><td rowspan="2">・ご住所</td></tr>
  <tr class="name"><td>・氏名</td></tr>
  <tr class="birth"><td>・生年月日<div class="era">S．H．　　　年　　　月　　　日</div></td><td>・電話番号</td></tr>
  <tr class="mail"><td colspan="2">・メールアドレス</td></tr>
  <tr class="pr"><td colspan="2">・自己PR</td></tr>
</table>

<div class="notes">
  <h3>〈注意事項〉</h3>
  <ol>
    <li><span>1</span><span>申し込み・キャンセルは6月7日（日）までにお願いします。</span></li>
    <li><span>2</span><span>男女比は出来る限り調整しますが同数にならないこともありますのでご了承願います。</span></li>
    <li><span>3</span><span>個人情報は厳重に管理し、本事業のみの使用とさせていただきます。</span></li>
    <li><span>4</span><span>悪天候時はプログラム内容を変更または中止する場合があります。</span></li>
  </ol>
  <p class="after">※申し込み受付後、事務局より順次詳細をお送りいたします。</p>
</div>

<div class="office">
  <strong>問い合わせ・お申込み</strong><br>
  汐見村商工会青年部事務局<br>
  〒100-0999 東京都汐見村汐見村2483番地<br>
  TEL：04992-7-4418　FAX：04992-7-5530<br>
  mail：shiomi@hx.nagisanet-example.jp
</div>
</body>
</html>
```